Postcard Design

I need a postcard to use as a mailer and handout piece to get a new vacation rental management company off the ground. This will be sent to rental property owners in Solvane on 30a in Florida.

A google image search of "Solvane 30A" will provide plenty of images for look and feel of the project. A quick google of "coastal modern design" will provide some feel for interiors and a color palette using the beachy but subtle colors typical to that decor.

Solvane is a 130 unit condominium complex in a very active beach rental market. The tone of the community is upscale family vacations...it is NOT a party destination. Beach and family time are what most people are here for.

Logo file uploaded here.

If good design comes in quickly I may zero in on one quickly to tweak it and get things moving.

Target audience is property owners who we hope to bring in as rental owners. The audience is not rental guests. Try to sell to property owners who you want to trust us with their investments.

We offer a full lineup of services including top-notch housekeeping, maintenance, marketing, and guest services.

We want to build relationships with our property owners.

We are a small team focused on only Solvane properties.

Designers...please feel free to suggest any wording or tag lines that you think sell this idea. Your creativity with the copy is as valuable as your visual creativity.

Some copy scraps & messaging to play with:

Tailored exclusively to Solvane and its owners

Boutique Rental Management

Full service maintenance and housekeeping

Solvane's reputation is our reputation

Thank you all.

I just updated he brief to provide some added guidance. Thanks!

Boutique

```html
<!DOCTYPE html>
<html lang="en">
<head>
<meta charset="utf-8">
<title>Solvane Boutique Rental Management Postcard</title>
<link rel="stylesheet" href="https://fonts.googleapis.com/css2?family=Cinzel:wght@400;700&family=EB+Garamond:wght@400&display=swap">
<style>
  :root {
    --paper: #ffffff;
    --ink: #1c2124;
    --band: #121618;
    --sea-deep: #3fa9a2;
    --sea-light: #8fd6cc;
    --sky-pale: #d9ecef;
    --sand: #d9b978;
    --facade: #c9a65a;
  }
  html, body {
    margin: 0;
    padding: 0;
    width: 1200px;
    height: 922px;
    overflow: hidden;
    background: var(--paper);
  }
  .postcard {
    position: relative;
    width: 1200px;
    height: 922px;
    background: var(--paper);
    color: var(--ink);
  }
  .services-intro {
    position: absolute;
    top: 52px;
    left: 0;
    width: 100%;
    margin: 0;
    text-align: center;
    font-family: "Cinzel", serif;
    color: var(--ink);
  }
  .services-intro .lead {
    display: block;
    font-size: 23px;
    font-weight: 400;
    letter-spacing: 0.5px;
    font-variant: small-caps;
    text-transform: lowercase;
  }
  .services-intro .lead::first-letter { text-transform: uppercase; }
  .services-intro .services-list {
    display: block;
    margin-top: 4px;
    font-size: 21px;
    font-weight: 700;
    letter-spacing: 0.6px;
  }
  .photo-band {
    position: absolute;
    top: 0;
    left: 0;
    width: 1200px;
    height: 922px;
  }
  .brand-name {
    position: absolute;
    top: 418px;
    left: 0;
    width: 100%;
    margin: 0;
    text-align: center;
    font-family: "EB Garamond", serif;
    font-weight: 400;
    font-size: 118px;
    line-height: 1;
    letter-spacing: 2px;
    color: var(--ink);
  }
  .selling-points {
    position: absolute;
    top: 650px;
    left: 0;
    width: 100%;
    margin: 0;
    padding: 0;
    list-style: none;
    text-align: center;
    font-family: "EB Garamond", serif;
    font-size: 25px;
    color: var(--ink);
  }
  .selling-points li {
    height: 56px;
    line-height: 34px;
  }
</style>
</head>
<body>
<main class="postcard">
  <h2 class="services-intro">
    <span class="lead">We offer a full lineup of services including top-notch</span>
    <span class="services-list">HOUSEKEEPING • MAINTENANCE • MARKETING • GUEST SERVICES</span>
  </h2>

  <svg class="photo-band" viewBox="0 0 1200 922" xmlns="http://www.w3.org/2000/svg">
    <defs>
      <linearGradient id="paddle-sea" x1="0" y1="0" x2="0" y2="1">
        <stop offset="0" stop-color="#4fb3ad"/>
        <stop offset="1" stop-color="#7ccfc3"/>
      </linearGradient>
      <linearGradient id="dune-view" x1="0" y1="0" x2="0" y2="1">
        <stop offset="0" stop-color="var(--sky-pale)"/>
        <stop offset="0.3" stop-color="var(--sea-light)"/>
        <stop offset="0.7" stop-color="#6f9f6a"/>
        <stop offset="1" stop-color="#7fd0d6"/>
      </linearGradient>
      <linearGradient id="pool-view" x1="0" y1="0" x2="0" y2="1">
        <stop offset="0" stop-color="#7fd3c6"/>
        <stop offset="0.35" stop-color="#e6eee8"/>
        <stop offset="0.5" stop-color="#b9ddd9"/>
        <stop offset="1" stop-color="#68c7c9"/>
      </linearGradient>
      <linearGradient id="wedding-walk" x1="0" y1="0" x2="1" y2="1">
        <stop offset="0" stop-color="var(--facade)"/>
        <stop offset="0.6" stop-color="#b48a4e"/>
        <stop offset="1" stop-color="#8a6a3e"/>
      </linearGradient>
    </defs>
    <path class="band" fill="var(--band)"
      d="M0 150 C 300 172, 560 192, 820 180 C 960 173, 1090 158, 1200 150
         L 1200 384 C 1080 398, 940 412, 780 418 C 520 424, 260 404, 0 396 Z"/>
    <rect role="img" aria-label="Paddleboarder on calm turquoise gulf water" x="0" y="188" width="305" height="166" fill="url(#paddle-sea)"/>
    <rect role="img" aria-label="Dune walkway with palm trees above the pool and gulf" x="305" y="192" width="309" height="182" fill="url(#dune-view)"/>
    <rect role="img" aria-label="Beachfront pool deck overlooking the gulf" x="614" y="210" width="275" height="170" fill="url(#pool-view)"/>
    <rect role="img" aria-label="Wedding couple on the boardwalk in front of the condominium" x="889" y="193" width="311" height="187" fill="url(#wedding-walk)"/>
  </svg>

  <h1 class="brand-name">Solvane</h1>

  <ul class="selling-points">
    <li>Tailored exclusively to Solvane and its owners</li>
    <li>Boutique Rental Management</li>
    <li>Full service maintenance and housekeeping</li>
    <li>Solvane's reputation is our reputation</li>
  </ul>
</main>
</body>
</html>
```